Global E-commerce Business Needs Banner Ad

We need banner ads for a fast growing E-commerce business cater mostly to women. The ads must have unique and beautiful background that accentuate the products. The ads should also have between 1-4 products in it. It needs to have the headline "Up To 80% Off Retail" in the ad. The ad also needs to have our logo and a "View Now" button. The ad should be more feminine and playful. Each product should have a different background design specially for the product to make it more beautiful.

Dimension: 320 by 480 pixel

Target Market(s)

Women

Industry/Entity Type

Business

Requirements
Must have
• 1) "Up To 80% Off Retail"
• 2) Brimvelle Logo
• 3) "View Now" button

```html
<!DOCTYPE html>
<html lang="en">
<head>
<meta charset="utf-8">
<title>Brimvelle Banner Ads</title>
<link rel="stylesheet" href="https://fonts.googleapis.com/css2?family=Noto+Serif:ital,wght@1,400;1,700&family=Josefin+Sans:wght@300&family=Parisienne&display=swap">
<style>
  :root {
    --stage: #ece8e3;
    --paper: #fbfbfb;
    --ink: #1a1a1a;
    --headline: #ffffff;
    --button-top: #1c1a1c;
    --button-bottom: #000000;
    --button-text: #d9d4d8;
    --rose-1: #f0a9c9;
    --rose-2: #e98fb8;
    --aqua-1: #8fd0df;
    --aqua-2: #5fb3cf;
    --silver-1: #f2f2f2;
    --silver-2: #9b9b9b;
    --silver-3: #5e5e5e;
    --blush-1: #f7c3dc;
    --blush-2: #c9a9c6;
    --blush-3: #8d7d93;
    --metal-light: #e6e6ea;
    --metal-mid: #a9a9b2;
    --gem-pink: #d9398a;
    --gem-blue: #4a8fd6;
    --gold: #d9a53a;
    --pave: #f4f4f4;
    --black-metal: #1d1a1f;
    --gem-soft-pink: #f27cc0;
  }
  * { box-sizing: border-box; margin: 0; padding: 0; }
  html, body { width: 1200px; height: 900px; overflow: hidden; }
  body { background: var(--stage); position: relative; font-family: "Noto Serif", serif; }

  .banner {
    position: absolute;
    top: 188px;
    width: 320px;
    height: 477px;
    background: var(--paper);
    overflow: hidden;
    box-shadow: 0 3px 10px rgba(0,0,0,0.25);
  }
  .banner--pastel { left: 75px; }
  .banner--sparkle { left: 436px; }
  .banner--petal { left: 800px; }

  .banner__visual { position: absolute; left: 0; top: 0; width: 320px; height: 477px; }
  .banner--pastel .banner__visual {
    background:
      radial-gradient(ellipse at 15% 15%, var(--rose-1) 0%, transparent 45%),
      radial-gradient(ellipse at 90% 85%, var(--rose-2) 0%, transparent 40%),
      linear-gradient(160deg, #f3b6cf 0%, #c7e3ee 40%, var(--aqua-1) 70%, var(--aqua-2) 100%);
  }
  .banner--sparkle .banner__visual {
    background:
      radial-gradient(ellipse at 50% 40%, var(--silver-1) 0%, #c8c8c8 35%, transparent 70%),
      linear-gradient(180deg, var(--silver-3) 0%, var(--silver-2) 45%, #bdbdbd 70%, var(--silver-3) 100%);
  }
  .banner--petal .banner__visual {
    background:
      radial-gradient(ellipse at 10% 70%, #f49cc4 0%, transparent 40%),
      radial-gradient(ellipse at 92% 25%, var(--blush-1) 0%, transparent 40%),
      linear-gradient(180deg, var(--blush-2) 0%, #b8a6bf 50%, var(--blush-3) 100%);
  }

  .product {
    position: absolute;
    border-radius: 46% 46% 42% 42%;
  }
  .banner--pastel .product {
    left: 88px; top: 130px; width: 146px; height: 212px;
    background:
      radial-gradient(circle at 50% 14%, var(--gem-pink) 0%, transparent 22%),
      radial-gradient(circle at 22% 24%, var(--gem-blue) 0%, transparent 18%),
      radial-gradient(circle at 80% 24%, var(--gem-blue) 0%, transparent 16%),
      radial-gradient(ellipse at 50% 60%, var(--metal-light) 0%, var(--metal-mid) 60%, rgba(169,169,178,0) 72%);
  }
  .banner--sparkle .product {
    left: 78px; top: 136px; width: 168px; height: 192px;
    background:
      radial-gradient(circle at 54% 12%, #ffffff 0%, transparent 18%),
      radial-gradient(ellipse at 40% 58%, var(--pave) 0%, #cfcfcf 28%, transparent 46%),
      radial-gradient(ellipse at 50% 58%, var(--gold) 0%, #b8862a 58%, rgba(184,134,42,0) 72%);
  }
  .banner--petal .product {
    left: 74px; top: 112px; width: 182px; height: 214px;
    background:
      radial-gradient(ellipse at 40% 12%, var(--gem-soft-pink) 0%, transparent 22%),
      radial-gradient(ellipse at 36% 52%, var(--gem-soft-pink) 0%, transparent 26%),
      radial-gradient(ellipse at 74% 58%, #f5a6d3 0%, transparent 20%),
      radial-gradient(ellipse at 50% 56%, #3a333d 0%, var(--black-metal) 58%, rgba(29,26,31,0) 72%);
  }

  .banner__frame { position: absolute; left: 0; top: 0; width: 320px; height: 477px; }

  .brand {
    position: absolute;
    top: 12px;
    left: 0;
    width: 320px;
    display: flex;
    justify-content: center;
    align-items: center;
    gap: 6px;
    font-family: "Josefin Sans", sans-serif;
    font-weight: 300;
    font-size: 27px;
    letter-spacing: 0.5px;
    text-transform: uppercase;
    color: var(--ink);
  }
  .brand__mark { width: 13px; height: 13px; background: var(--ink); }

  .headline {
    position: absolute;
    top: 79px;
    left: 0;
    width: 320px;
    text-align: center;
    font-family: "Noto Serif", serif;
    font-style: italic;
    font-weight: 700;
    font-size: 21px;
    color: var(--headline);
    text-shadow: 0 1px 3px rgba(0,0,0,0.35);
  }
  .banner--petal .headline { font-weight: 400; }

  .cta {
    position: absolute;
    left: 34px;
    top: 404px;
    width: 252px;
    height: 56px;
    background: linear-gradient(180deg, var(--button-top), var(--button-bottom));
    border: 1px solid #444;
    display: flex;
    align-items: center;
    justify-content: center;
    font-family: "Parisienne", cursive;
    font-size: 36px;
    color: var(--button-text);
    text-decoration: none;
  }
</style>
</head>
<body>

  <section class="banner banner--pastel">
    <div class="banner__visual" role="img" aria-label="Soft pink and aqua floral backdrop"></div>
    <div class="product" role="img" aria-label="Silver ring with a pink centre stone, blue side stones and pink stones along the band"></div>
    <svg class="banner__frame" viewBox="0 0 320 477" aria-hidden="true">
      <polygon points="0,0 320,0 320,40 160,62 0,40" fill="#fbfbfb"/>
      <path d="M0,432 Q160,446 320,428 L320,477 L0,477 Z" fill="#fbfbfb"/>
    </svg>
    <div class="brand"><span class="brand__mark"></span>Brimvelle</div>
    <h2 class="headline">Up To 80% Off Retail</h2>
    <a class="cta" href="#">View Now</a>
  </section>

  <section class="banner banner--sparkle">
    <div class="banner__visual" role="img" aria-label="Misty silver backdrop with sparkling strands"></div>
    <div class="product" role="img" aria-label="Gold and silver ring with a solitaire stone and a pavé set band"></div>
    <svg class="banner__frame" viewBox="0 0 320 477" aria-hidden="true">
      <polygon points="0,0 320,0 320,40 160,62 0,40" fill="#fbfbfb"/>
      <path d="M0,432 Q160,446 320,428 L320,477 L0,477 Z" fill="#fbfbfb"/>
    </svg>
    <div class="brand"><span class="brand__mark"></span>Brimvelle</div>
    <h2 class="headline">Up To 80% Off Retail</h2>
    <a class="cta" href="#">View Now</a>
  </section>

  <section class="banner banner--petal">
    <div class="banner__visual" role="img" aria-label="Pink petal backdrop"></div>
    <div class="product" role="img" aria-label="Black ring pair set with pink and white stones"></div>
    <svg class="banner__frame" viewBox="0 0 320 477" aria-hidden="true">
      <polygon points="0,0 320,0 320,40 160,62 0,40" fill="#fbfbfb"/>
      <path d="M0,432 Q160,446 320,428 L320,477 L0,477 Z" fill="#fbfbfb"/>
    </svg>
    <div class="brand"><span class="brand__mark"></span>Brimvelle</div>
    <h2 class="headline">Up To 80% Off Retail</h2>
    <a class="cta" href="#">View Now</a>
  </section>

</body>
</html>
```